Business card design for Velvet Harbor

We need business cards designed for our new marketing consulting company, Velvet Harbor. Our services include marketing strategy, go-to-market and launch planning, growth strategy, and execution. We serve medical technology and health technology companies, from startups to well-established growth companies.

The business cards should feel professional, credible, reliable and trustworthy, and should instill confidence. Also bold, creative, and modern.

The design must use the Velvet Harbor logo.

The primary brand color is this orange: #FF5501
A secondary color that you can use is this gray: #282B2D
I would prefer only to use the orange and gray. But if you feel you really need an additional accent color (please use it very sparingly, as little as possible), you can use this blue for small accent purposes: #009FED

Attached are the logo files. The main logo is the one with a little bit of orange on the left and the rest is gray.

The business card should include the following:

Velvet Harbor logo
First name and last name
Title
Email address
Phone number and type (in whatever order looks best for the design
Website (the website does not need to be in the same block as the personal info)

For example:

Nessa Pryle
Founder & Principal
nessa@velvetharbor.com
+1.628.309.4156 mobile (can use "." or spaces in between blocks of numbers)
velvetharbor.com (somewhere on the card, it does not need to be with the personal info; and note that there is no "www." at the beginning)

Note that there will be no address listed on the business card.

Target Market(s)

Executives (CEO, head of marketing, head of sales) at medical technology and health technology companies, mostly in their 40s and older, well-educated, often with advanced degrees. They are strategic thinkers, responsible for budgets, and familiar with P&L. Their comfort with and trust in using outside consultants varies.

Industry/Entity Type

Medical technology and health technology companies.

Contact Information for Business Card

See project description

Font styles to use
Sans Serif

Requirements
Must have
• Logo and see Business card details section above.

```html
<!DOCTYPE html>
<html lang="en">
<head>
<meta charset="utf-8">
<title>Velvet Harbor — Business Card</title>
<link rel="stylesheet" href="https://fonts.googleapis.com/css2?family=Montserrat:wght@400;500;700&display=swap">
<style>
  :root {
    --brand-orange: #F15A22;
    --card-gray: #282B2D;
    --paper-white: #FFFFFF;
    --backdrop: #B9B9B9;
    --backdrop-light: #CFCFCF;
  }
  * { box-sizing: border-box; margin: 0; padding: 0; }
  html, body { width: 1200px; height: 815px; overflow: hidden; }
  body {
    background: linear-gradient(180deg, var(--backdrop-light), var(--backdrop));
    font-family: "Montserrat", sans-serif;
    position: relative;
  }
  .card {
    position: absolute;
    top: 252px;
    width: 540px;
    height: 311px;
    background: var(--card-gray);
    border-radius: 22px;
    border-bottom: 5px solid var(--brand-orange);
    box-shadow: 0 18px 40px rgba(0,0,0,0.28);
    overflow: hidden;
    color: var(--paper-white);
  }
  .card--front { left: 40px; }
  .card--back { left: 620px; }

  .brand-name {
    font-family: "Montserrat", sans-serif;
    font-weight: 700;
    color: var(--paper-white);
    text-transform: uppercase;
    line-height: 1.1;
    letter-spacing: 0.04em;
  }
  .card--front .brand-name--small {
    position: absolute;
    left: 40px;
    top: 44px;
    font-size: 24px;
  }
  .card--front .brand-feature {
    position: absolute;
    left: 290px;
    top: 40px;
    width: 210px;
    height: 150px;
    display: flex;
    align-items: center;
    justify-content: center;
  }
  .card--front .brand-feature .brand-name {
    font-size: 36px;
    text-align: center;
  }

  .accent-bar {
    position: absolute;
    left: 0;
    top: 150px;
    width: 9px;
    height: 44px;
    background: var(--brand-orange);
  }
  .person {
    position: absolute;
    left: 40px;
    top: 148px;
  }
  .person__name {
    font-weight: 700;
    font-size: 23px;
    color: var(--brand-orange);
    text-transform: uppercase;
    letter-spacing: 0.01em;
  }
  .person__title {
    font-weight: 500;
    font-size: 13px;
    letter-spacing: 0.02em;
    margin-top: 2px;
  }
  .divider {
    position: absolute;
    left: 72px;
    top: 207px;
    width: 12px;
    height: 1px;
    background: var(--brand-orange);
  }
  .contact-list {
    position: absolute;
    left: 72px;
    top: 222px;
    list-style: none;
  }
  .contact-list li {
    display: flex;
    align-items: center;
    gap: 9px;
    font-size: 13px;
    font-weight: 400;
    line-height: 1;
    margin-bottom: 9px;
  }
  .contact-list svg { width: 11px; height: 11px; fill: var(--brand-orange); flex: none; }

  .card--back .brand-lockup {
    position: absolute;
    left: 50%;
    top: 50%;
    transform: translate(-50%, -50%);
  }
  .card--back .brand-name {
    font-size: 36px;
  }
</style>
</head>
<body>

  <section class="card card--front" aria-label="Card front">
    <div class="brand-name brand-name--small">Velvet<br>Harbor</div>
    <div class="brand-feature">
      <div class="brand-name">Velvet<br>Harbor</div>
    </div>
    <span class="accent-bar"></span>
    <div class="person">
      <p class="person__name">Nessa Pryle</p>
      <p class="person__title">Founder &amp; Principal</p>
    </div>
    <span class="divider"></span>
    <ul class="contact-list">
      <li>
        <svg viewBox="0 0 24 24" aria-hidden="true"><path d="M6.6 10.8a15.1 15.1 0 0 0 6.6 6.6l2.2-2.2c.3-.3.7-.4 1-.2 1.1.4 2.3.6 3.6.6.6 0 1 .4 1 1V20c0 .6-.4 1-1 1A17 17 0 0 1 3 4c0-.6.4-1 1-1h3.5c.6 0 1 .4 1 1 0 1.3.2 2.5.6 3.6.1.3 0 .7-.2 1z"/></svg>
        <span>+1.628.309.4156</span>
      </li>
      <li>
        <svg viewBox="0 0 24 24" aria-hidden="true"><path d="M2 5h20v14H2z"/><path d="M3 6l9 7 9-7v-1H3z" fill="#282B2D"/></svg>
        <span>nessa@velvetharbor.com</span>
      </li>
      <li>
        <svg viewBox="0 0 24 24" aria-hidden="true"><circle cx="12" cy="12" r="10"/><path d="M2 12h20M12 2c3 3 3 17 0 20M12 2c-3 3-3 17 0 20" stroke="#282B2D" stroke-width="1.6" fill="none"/></svg>
        <span>velvetharbor.com</span>
      </li>
    </ul>
  </section>

  <section class="card card--back" aria-label="Card back">
    <div class="brand-lockup">
      <div class="brand-name">Velvet<br>Harbor</div>
    </div>
  </section>

</body>
</html>
```